依頼詳細
サイトURL
http://www.nemira-eng.example
ページ数
1ページ
希望イメージ
シンプル 複雑
単色 カラフル
暗い 明るい
日常 高級
遊び心 厳粛
未来的 伝統的
女性的 男性的
希望する色
納品ファイル
• 高解像度JPG (.jpg)
• イラストレーター形式 (.ai)
• フォトショップ形式 (.psd)
補足説明
依頼時に登録した内容がきえてしまいましたので、再アップします。

食料品パッケージなどに書いてある賞味期限など、包装時に個別に印刷
する場合につかう業務用プリンターのメーカーです。一般の方の目に
触れることはありませんが、大手企業をメインに数多く使われています。

ホームページリニューアルにつき、トップページのデザインを募集します。
添付資料に企画時のデザイン案がありますので、メニュー項目等を参考に
してください。レイアウトについては資料を踏襲する必要はありません。
横幅は900ピクセルにしてください。

ロゴ、写真などは添付してあります。

現行のサイトはかなり以前にデザインされたものなので、テーマカラー等
の参考にはなりません。(内容に関しては更新されています。)

業務用ということで、製品が地味です。この路線でいくと暗くなりそうです。
食品・流通・包装のイメージで明るくしていくと好まれると思います。

よろしくお願い致します。
すみません、数名の方から期間が短すぎるとご連絡をいただいたので、2日だけ延長します。
■ 選んだ理由

トップ下の製品一覧がクライアントに好評でした。

■ 提案者全員のお礼・コメント

この度は短期間であったにも関わらず、数多くの皆様にご提案いただきありがとうございました。
今後ともよろしくお願い致します。

```html
<!DOCTYPE html>
<html lang="ja">
<head>
<meta charset="utf-8">
<title>NEMIRA ネミラエンジニアリング</title>
<link rel="stylesheet" href="https://fonts.googleapis.com/css2?family=Noto+Sans+JP:wght@400;700&display=swap">
<style>
:root{
  --red:#c8161d;
  --red-dark:#8e0d12;
  --ink:#333;
  --muted:#777;
  --line:#ddd;
  --pale:#f4f4f4;
  --white:#fff;
}
*{box-sizing:border-box;margin:0;padding:0}
html,body{width:841px;height:1200px;overflow:hidden;background:var(--white)}
body{font-family:"Noto Sans JP",sans-serif;color:var(--ink);font-size:10px;line-height:1.6}
.page{width:841px;height:1200px;position:relative}

.site-header{height:62px;position:relative}
.brand{display:flex;align-items:center;gap:5px;color:var(--red);font-weight:700;font-size:26px;letter-spacing:1px;line-height:1}
.brand-mark{width:10px;height:10px;background:var(--red)}
.site-header .brand{position:absolute;left:24px;top:6px}
.tagline{position:absolute;left:150px;top:5px;font-size:7.5px;color:var(--muted);line-height:1.45}
.global-nav{position:absolute;left:0;right:0;top:38px;height:24px;background:var(--red);display:flex;padding-left:24px}
.global-nav a{color:var(--white);text-decoration:none;font-size:9px;font-weight:700;width:110px;display:flex;align-items:center;justify-content:center;border-right:1px solid rgba(255,255,255,.35)}
.global-nav a.current{background:var(--red-dark)}

.hero{height:184px;background:linear-gradient(180deg,#fafafa,#e9e9e9);position:relative;padding:40px 40px;border-bottom:1px solid var(--line)}
.hero h1{font-size:24px;line-height:1.4;font-weight:700;color:var(--red)}
.hero p{font-size:9px;margin-top:12px;width:330px;color:#555}
.hero-visual{position:absolute;right:30px;top:10px;width:330px;height:164px;background:linear-gradient(135deg,#f0f0f0,#8a8a8a)}

.section{padding:0 24px}
.section-title{display:flex;align-items:center;gap:6px;font-size:11px;font-weight:700;border-bottom:2px solid var(--red);padding-bottom:3px;margin-top:16px}
.section-title::before{content:"";width:8px;height:8px;background:var(--red)}
.section-title small{font-weight:400;color:var(--muted);font-size:8.5px}
.products{display:grid;grid-template-columns:repeat(3,1fr);gap:14px;margin-top:10px}
.product{display:flex;gap:8px;padding:4px;height:84px}
.product-text{font-size:8px;flex:1;border:1px solid var(--line);padding:6px;height:54px}
.product-text strong{display:block;color:var(--red);font-size:9px;margin-bottom:2px}
.product-img{width:110px;height:76px;background:linear-gradient(135deg,#ececec,#8f8f8f)}
.product-links{display:grid;grid-template-columns:repeat(6,auto);justify-content:start;gap:4px 26px;margin-top:8px;font-size:8.5px;padding:6px 10px;border-top:1px solid var(--line);border-bottom:1px solid var(--line)}
.product-links span::before{content:"■ ";color:var(--red);font-size:6px}

.news{margin-top:6px}
.news li{list-style:none;display:flex;gap:20px;font-size:8.5px;padding:4px 6px;border-bottom:1px dotted var(--line)}
.news time{color:var(--muted);width:64px}
.intro{font-size:8.5px;margin-top:8px;line-height:2;color:#555}

.site-footer{position:absolute;left:0;right:0;top:740px;height:420px;border-top:3px solid var(--red);padding:18px 24px;display:flex;gap:34px}
.company .brand{font-size:22px}
.company-name{font-size:7.5px;margin:4px 0 10px}
.company dl{font-size:7.5px;line-height:1.55;color:#555}
.company dt{font-weight:700;color:var(--ink);margin-top:6px}
.footer-col h3{font-size:9px;color:var(--red);margin-bottom:4px}
.footer-col ul{list-style:none;font-size:8px;line-height:1.9;color:#555;margin-bottom:12px}
.footer-col li::before{content:"■ ";color:var(--red);font-size:6px}
.copyright{position:absolute;left:0;right:0;bottom:0;height:40px;border-top:2px solid var(--red);color:var(--muted);font-size:7.5px;display:flex;align-items:center;justify-content:space-between;padding:0 24px}
</style>
</head>
<body>
<div class="page">
  <header class="site-header">
    <div class="brand"><span class="brand-mark"></span>NEMIRA</div>
    <p class="tagline">賞味期限・製造番号などの印字を支える業務用プリンターメーカー<br>食品・流通・包装の現場に最適な印字システムをお届けします。</p>
    <nav class="global-nav">
      <a class="current">トップページ</a><a>サーマルプリンタ</a><a>ホットプリンタ</a><a>サプライプリンタ</a><a>会社概要</a><a>お問い合わせ</a>
    </nav>
  </header>

  <section class="hero">
    <h1>お客様のニーズに沿った<br>最適の方法をご提案します。</h1>
    <p>食品パッケージの賞味期限や製造番号など、包装時に個別に印字するための業務用プリンターを、豊富な実績と技術でご提供しています。</p>
    <div class="hero-visual" role="img" aria-label="業務用プリンター製品の写真"></div>
  </section>

  <section class="section">
    <h2 class="section-title">製品一覧 <small>Products</small></h2>
    <div class="products">
      <div class="product"><div class="product-text"><strong>サーマルプリンタ</strong>高速・高精細な印字を実現します。</div><div class="product-img" role="img" aria-label="サーマルプリンタの写真"></div></div>
      <div class="product"><div class="product-text"><strong>ホットプリンタ</strong>フィルムへ鮮明に日付を印字します。</div><div class="product-img" role="img" aria-label="ホットプリンタの写真"></div></div>
      <div class="product"><div class="product-text"><strong>サプライプリンタ</strong>リボン・インクなどを揃えています。</div><div class="product-img" role="img" aria-label="サプライ製品の写真"></div></div>
    </div>
    <div class="product-links">
      <span>小型印字機</span><span>熱転写機</span><span>大型印字機</span><span>インクジェットプリンタ</span><span>搬送装置</span><span>自動検査機</span><span>日付印字機</span><span>サプライ</span><span>オプション機器</span>
    </div>

    <h2 class="section-title">ニュースリリース <small>News</small></h2>
    <ul class="news">
      <li><time>2011.09.28</time>新型サーマルプリンタの販売を開始いたしました。詳しくは製品ページをご覧ください。</li>
      <li><time>2011.09.27</time>包装機械展示会への出展のお知らせを掲載しました。</li>
      <li><time>2011.09.26</time>ホームページをリニューアルいたしました。</li>
    </ul>

    <h2 class="section-title">○○紹介</h2>
    <p class="intro">食品や日用品のパッケージに記載される賞味期限・製造番号などを、包装工程で一つひとつ正確に印字するための業務用プリンターを開発しています。高速ラインにも対応する安定した性能と、現場に寄り添うサポート体制で、多くのお客様に長くご利用いただいています。用途や設置環境に合わせて最適な機種とオプションをご提案いたします。導入前のテスト印字から設置、操作説明、定期点検まで一貫して対応いたします。</p>

    <h2 class="section-title">○○紹介</h2>
    <p class="intro">消耗品の供給や部品交換もスピーディーに行い、生産ラインを止めない運用をお手伝いします。お気軽にお問い合わせください。</p>
  </section>

  <footer class="site-footer">
    <div class="company">
      <div class="brand"><span class="brand-mark"></span>NEMIRA</div>
      <p class="company-name">ネミラエンジニアリング株式会社</p>
      <dl>
        <dt>本社・工場</dt><dd>〒100-0001 東京都架空区中央1-2-3<br>TEL 03-0000-1234</dd>
        <dt>大阪営業所</dt><dd>〒530-0001 大阪府架空市北町4-5-6<br>TEL 06-0000-5678</dd>
        <dt>名古屋営業所</dt><dd>〒460-0001 愛知県架空市栄町7-8-9<br>TEL 052-000-9012</dd>
      </dl>
    </div>
    <div class="footer-col">
      <h3>会社情報</h3><ul><li>会社概要</li><li>沿革</li><li>事業所</li><li>採用情報</li></ul>
      <h3>製品一覧</h3><ul><li>サーマルプリンタ</li><li>ホットプリンタ</li><li>サプライ</li></ul>
    </div>
    <div class="footer-col">
      <h3>最新情報</h3><ul><li>ニュース</li><li>展示会</li><li>技術情報</li></ul>
      <h3>ホットプリンタ</h3><ul><li>HP-100</li><li>HP-200</li><li>HP-300</li></ul>
    </div>
    <div class="footer-col">
      <h3>お問い合わせ</h3><ul><li>資料請求</li><li>お見積もり</li><li>サポート窓口</li></ul>
      <h3>インクジェット</h3><ul><li>IJ-10</li><li>IJ-20</li><li>オプション</li></ul>
    </div>
  </footer>
  <div class="copyright"><span>http://www.nemira-eng.example</span><span>Copyright © NEMIRA ENGINEERING CO., LTD. All Rights Reserved.</span></div>
</div>
</body>
</html>
```